Harwick Assurance Partners Ltd needs a business card and logo

We need a logo for documents, invoices etc and a business card to match. We are a health auditing, training and consulting company based in Tasmere and working in both Australia and Tasmere. We ensure health organisations meet all their compliance requirements and develop expertise in the health auditing sector. The design should in some way reflect either symbols for quality management in the health sector.

Target Market(s)

Health providers and those wishing to increase their capability in meeting and understanding compliance requirements

Industry/Entity Type

Business

Contact Information for Business Card

Logo plus contact details

Logo Text

Health auditing, consultancy and training

Requirements
Must have
• Name and contact details director: Molly Strand, mstrand@hap-example.co.nz, PO Box 318, Kowhai Heights, Tasmere, cell +6427391065

```html
<!DOCTYPE html>
<html lang="en">
<head>
<meta charset="utf-8">
<title>Harwick Assurance Partners – Business Card</title>
<link href="https://fonts.googleapis.com/css2?family=Libre+Baskerville&family=Montserrat:wght@600&display=swap" rel="stylesheet">
<style>
  :root{
    --bg:#e9e7e3;
    --card:#ffffff;
    --green:#8cc63f;
    --blue:#29b6e6;
    --orange:#f5a623;
    --pink:#e6197a;
    --ink:#4a4a4a;
    --white:#ffffff;
  }
  *{box-sizing:border-box;margin:0;padding:0}
  html,body{width:1200px;height:900px;overflow:hidden;background:var(--bg)}
  .canvas{width:1200px;height:900px;display:flex;align-items:center;justify-content:center}
  .card{
    position:relative;width:1000px;height:572px;background:var(--card);
    box-shadow:0 10px 30px rgba(0,0,0,.18);overflow:hidden;
  }
  .brand{position:absolute;left:56px;top:52px;display:flex;align-items:center;gap:22px}
  .brand-dot{width:96px;height:96px;border-radius:50%;background:var(--green)}
  .brand-name{
    font-family:"Libre Baskerville",serif;font-size:26px;line-height:1.25;color:var(--ink);
  }
  .ribbon{
    position:absolute;left:0;height:60px;background:var(--green);
    clip-path:polygon(0 0,calc(100% - 26px) 0,100% 50%,calc(100% - 26px) 100%,0 100%);
    display:flex;align-items:center;gap:16px;padding-left:70px;color:var(--white);
    font-family:"Libre Baskerville",serif;font-size:25px;letter-spacing:1.5px;white-space:nowrap;
  }
  .ribbon--name{top:268px;width:440px;font-family:"Montserrat",sans-serif;font-weight:600;font-variant:small-caps;font-size:30px;letter-spacing:2px}
  .ribbon--phone{top:336px;width:540px}
  .ribbon--email{top:404px;width:650px}
  .ribbon--address{top:472px;width:760px}
  .icon{flex:none}
  .edge-stripe{position:absolute;left:0;bottom:0;width:100%;height:22px;display:flex}
  .edge-stripe span{height:100%}
  .edge-green{background:var(--green);width:46%}
  .edge-blue{background:var(--blue);width:16%}
  .edge-orange{background:var(--orange);width:18%}
  .edge-pink{background:var(--pink);width:20%}
</style>
</head>
<body>
<main class="canvas">
  <section class="card">
    <div class="brand">
      <div class="brand-dot"></div>
      <div class="brand-name">Harwick Assurance<br>Partners Ltd</div>
    </div>

    <div class="ribbon ribbon--name">Molly Strand</div>

    <div class="ribbon ribbon--phone">
      <svg class="icon" width="34" height="30" viewBox="0 0 34 30" aria-hidden="true">
        <rect x="1" y="1" width="32" height="28" rx="6" fill="#fff"/>
        <path d="M11 8c1.5-1 3 2 3.2 3 .2 1-1.5 1.6-1 2.6.8 1.7 2.4 3.3 4.2 4 1 .4 1.6-1.3 2.6-1.1 1 .2 4 1.8 3 3.3-1.3 2-4 2.4-7 .6-3-1.8-5.3-4.4-6.2-7.4-.6-2.2.2-4.1 1.2-5z" fill="#8cc63f"/>
      </svg>
      <span>: +6427391065</span>
    </div>

    <div class="ribbon ribbon--email">
      <svg class="icon" width="46" height="30" viewBox="0 0 46 30" aria-hidden="true">
        <rect x="2" y="2" width="42" height="26" fill="none" stroke="#fff" stroke-width="3"/>
        <path d="M2 2l21 15L44 2" fill="none" stroke="#fff" stroke-width="3"/>
      </svg>
      <span>: mstrand@hap-example.co.nz</span>
    </div>

    <div class="ribbon ribbon--address"><span>PO Box 318, Kowhai Heights, Tasmere,</span></div>

    <div class="edge-stripe">
      <span class="edge-green"></span><span class="edge-blue"></span><span class="edge-orange"></span><span class="edge-pink"></span>
    </div>
  </section>
</main>
</body>
</html>
```